Tradeshow Banner Design (Qty2, 6'H x 2'W)

Brightwell Contractors is an Electrical, Fire Alarm, and Security Contracting company. For tradeshows, we would like 2 vertical Banners to put behind our booth. Our colors are Red, Grey & Black. I would like the Banners to be informative on what services we provide, with some appealing Graphic Design. (bwc-kmo.com)
Slogan: Safeguarding Communities Electrical, Fire & Security Solutions
Target Market(s)
Commercial Construction Clients
Industry/Entity Type
Electrical / Construction
Font styles to use
Other font styles liked:
- Aileron
Colors
EB3D1F
EC4F4E
F09395
F8D3D4
FCEDEE
Requirements
Must have
- Our Logo, Color Scheme, Brief Caption of the services we provide
Nice to have
- Appealing Imagery & a modern/simplistic design

```html
<!DOCTYPE html>
<html lang="en">
<head>
<meta charset="utf-8">
<title>Brightwell Contractors – Tradeshow Banners</title>
<link rel="stylesheet" href="https://fonts.googleapis.com/css2?family=Montserrat:wght@400;500;700&family=Roboto:wght@700;900&display=swap">
<style>
  :root {
    --red: #eb3d1f;
    --coral: #ec4f4e;
    --rose: #f09395;
    --blush: #f8d3d4;
    --paper: #fcedee;
    --grey: #4a4a50;
    --ink: #2b2b2f;
    --stage: #d9d9db;
    --white: #ffffff;
  }
  * { box-sizing: border-box; margin: 0; padding: 0; }
  html, body { width: 871px; height: 1200px; overflow: hidden; }
  body { background: var(--stage); font-family: "Montserrat", sans-serif; color: var(--ink); }
  .canvas { position: relative; width: 871px; height: 1200px; overflow: hidden; }

  .banner {
    position: absolute; top: 63px; width: 358px; height: 1074px;
    background: var(--paper); overflow: hidden;
    box-shadow: 0 4px 14px rgba(0,0,0,.18);
  }
  .banner--left { left: 68px; }
  .banner--right { left: 445px; }

  .brand { position: absolute; left: 89px; top: 37px; display: flex; align-items: center; gap: 8px; }
  .brand__dot { width: 74px; height: 74px; border-radius: 50%; background: var(--red); flex: none; }
  .brand__text { display: flex; flex-direction: column; }
  .brand__name { font-weight: 700; font-size: 17px; line-height: 1.05; color: var(--grey); letter-spacing: .3px; }
  .brand__tag { font-weight: 500; font-size: 7.5px; color: var(--grey); margin-top: 4px; letter-spacing: .3px; }

  .photo { position: absolute; border-radius: 50%; }
  .photo--electrical { left: 124px; top: 196px; width: 288px; height: 288px; background: radial-gradient(circle at 60% 45%, #f2b13a 0%, #c8653a 35%, var(--coral) 70%); }
  .photo--security { left: -80px; top: 552px; width: 287px; height: 287px; background: radial-gradient(circle at 55% 40%, #e6e6e6 0%, #bdbdbd 30%, var(--coral) 65%); }
  .photo--fire { left: -80px; top: 183px; width: 288px; height: 288px; background: radial-gradient(circle at 55% 40%, var(--red) 0%, #ef7a23 45%, #f39a2a 75%); }
  .photo--access { left: 124px; top: 549px; width: 287px; height: 287px; background: radial-gradient(circle at 45% 45%, #f4f4f4 0%, #d8d8d8 35%, var(--coral) 68%); }

  .heading {
    position: absolute; font-family: "Roboto", sans-serif; font-weight: 900;
    color: var(--red); font-size: 43px; line-height: 37px; letter-spacing: -1px; text-transform: uppercase;
  }
  .heading--right { text-align: right; }

  .rail { position: absolute; width: 1.5px; background: var(--red); }
  .rail__node { position: absolute; left: -4px; width: 9px; height: 9px; border-radius: 50%; border: 1.5px solid var(--red); background: var(--paper); }

  .service { position: absolute; }
  .service__title { font-weight: 500; font-size: 12px; line-height: 11px; color: var(--ink); margin-bottom: 7px; }
  .service__list { list-style: none; font-size: 6.1px; line-height: 6.5px; color: var(--ink); }
  .service__list li { margin-bottom: 4px; padding-left: 5px; position: relative; }
  .service__list li::before { content: "-"; position: absolute; left: 0; color: var(--rose); }

  .footer { position: absolute; left: 0; bottom: 0; width: 358px; height: 121px; background: var(--coral); color: var(--white); }
  .footer__cta { position: absolute; left: 26px; top: 13px; font-family: "Roboto", sans-serif; font-weight: 700; font-size: 12.6px; letter-spacing: -.35px; white-space: nowrap; }
  .footer__areas { position: absolute; left: 27px; top: 40px; font-size: 9.4px; line-height: 10.5px; font-weight: 700; text-transform: uppercase; }
  .footer__areas span { font-weight: 400; }
  .footer__contact { position: absolute; right: 27px; top: 40px; text-align: right; font-weight: 700; }
  .footer__line { display: flex; justify-content: flex-end; align-items: center; gap: 3px; font-size: 9px; line-height: 13px; }
  .footer__line--addr { font-size: 6.3px; line-height: 7px; margin-top: 2px; align-items: flex-start; }
  .footer__line svg { flex: none; }
  .footer__social { position: absolute; top: 95px; display: flex; align-items: center; gap: 4px; font-size: 9px; }
  .footer__social--left { left: 27px; }
  .footer__social--right { right: 27px; }
  .social-mark { width: 8px; height: 8px; background: var(--white); }
</style>
</head>
<body>
<div class="canvas">

  <section class="banner banner--left">
    <div class="brand">
      <div class="brand__dot"></div>
      <div class="brand__text">
        <span class="brand__name">BRIGHTWELL<br>CONTRACTORS</span>
        <span class="brand__tag">ELECTRICAL | FIRE | SECURITY</span>
      </div>
    </div>

    <div class="photo photo--electrical" role="img" aria-label="Electrician's hands writing on a clipboard above a tool belt with multimeter and screwdrivers"></div>

    <div class="rail" style="left:23px; top:165px; height:270px;">
      <span class="rail__node" style="top:152px;"></span>
      <span class="rail__node" style="top:261px;"></span>
    </div>
    <h2 class="heading" style="left:33px; top:163px;">ELECT-<br>RICAL</h2>

    <div class="service" style="left:35px; top:315px; width:86px;">
      <h3 class="service__title">Electrical<br>Installation<br>&amp; Repair</h3>
      <ul class="service__list">
        <li>Full electrical services</li>
        <li>Licensed Electricians</li>
        <li>LED retrofitting expertise</li>
        <li>Versatile one-stop-shop for customer satisfaction</li>
        <li>24/7 emergency repairs</li>
      </ul>
    </div>
    <div class="service" style="left:35px; top:426px; width:165px;">
      <h3 class="service__title">Structured<br>Wiring</h3>
      <ul class="service__list">
        <li>Speeds up businesses with wiring solutions</li>
        <li>Expert installation for seamless security, networking</li>
        <li>Professional, wire-free look</li>
        <li>Boosts tech adoption confidence</li>
      </ul>
    </div>

    <div class="photo photo--security" role="img" aria-label="White outdoor CCTV security camera on a mounting bracket"></div>

    <div class="rail" style="left:334px; top:536px; height:290px;">
      <span class="rail__node" style="top:184px;"></span>
      <span class="rail__node" style="top:282px;"></span>
    </div>
    <h2 class="heading heading--right" style="right:39px; top:534px;">SECU-<br>RITY</h2>

    <div class="service" style="left:223px; top:718px; width:105px;">
      <h3 class="service__title">Security<br>Monitoring</h3>
      <ul class="service__list">
        <li>Fast emergency alarm response</li>
        <li>Varied security/fire systems</li>
        <li>Wireless connectivity persists during power cuts</li>
        <li>Motion detectors and sensors</li>
        <li>Manual trigger option</li>
      </ul>
    </div>
    <div class="service" style="left:223px; top:817px; width:105px;">
      <h3 class="service__title">Surveillance</h3>
      <ul class="service__list">
        <li>Monitoring via CCTV/IP cameras</li>
        <li>Ensures premises and staff safety</li>
        <li>Cellular-connected cameras allow recording during outages</li>
        <li>Accessible via smartphones</li>
        <li>Enhances business control</li>
      </ul>
    </div>

    <footer class="footer">
      <p class="footer__cta">LET US HELP YOU PROTECT YOUR BUSINESS TODAY</p>
      <p class="footer__areas"><span>SERVING</span> AUBURN, KENT,<br>RENTON, SEATTLE, BELLEVUE,<br>LYNNWOOD, MAPLE VALLEY,<br>COVINGTON, PUYALLUP</p>
      <div class="footer__contact">
        <p class="footer__line"><svg width="8" height="8" viewBox="0 0 10 10"><circle cx="5" cy="5" r="5" fill="#fff"/><path d="M3 2.5l1 1-.6.8a4 4 0 0 0 2.3 2.3l.8-.6 1 1-.8.9C4.8 7.6 2.4 5.2 2.1 3.3z" fill="#ec4f4e"/></svg>253-555-0142</p>
        <p class="footer__line"><svg width="8" height="8" viewBox="0 0 10 10"><circle cx="5" cy="5" r="4.3" fill="none" stroke="#fff" stroke-width="1.2"/><rect x="2.8" y="3.4" width="4.4" height="3.2" fill="none" stroke="#fff" stroke-width=".8"/><path d="M2.8 3.4L5 5.2l2.2-1.8" fill="none" stroke="#fff" stroke-width=".8"/></svg>office@bwc-kmo.com</p>
        <p class="footer__line footer__line--addr"><svg width="8" height="9" viewBox="0 0 10 12"><path d="M5 0a4 4 0 0 1 4 4c0 3-4 8-4 8S1 7 1 4a4 4 0 0 1 4-4z" fill="#fff"/><circle cx="5" cy="4" r="1.5" fill="#ec4f4e"/></svg><span>2210 Cedar Ridge Pkwy SE STE 210<br>Harborview, WA 98021</span></p>
      </div>
      <p class="footer__social footer__social--left"><span class="social-mark"></span>bwc_kmo</p>
      <p class="footer__social footer__social--right"><span class="social-mark"></span>BrightwellContractors</p>
    </footer>
  </section>

  <section class="banner banner--right">
    <div class="brand">
      <div class="brand__dot"></div>
      <div class="brand__text">
        <span class="brand__name">BRIGHTWELL<br>CONTRACTORS</span>
        <span class="brand__tag">ELECTRICAL | FIRE | SECURITY</span>
      </div>
    </div>

    <div class="photo photo--fire" role="img" aria-label="Gloved firefighter in orange suit holding a red fire extinguisher"></div>

    <div class="rail" style="left:335px; top:136px; height:250px;">
      <span class="rail__node" style="top:166px;"></span>
      <span class="rail__node" style="top:244px;"></span>
    </div>
    <h2 class="heading heading--right" style="right:38px; top:136px;">FIRE<br>PROTE-<br>CTION</h2>

    <div class="service" style="left:223px; top:295px; width:105px;">
      <h3 class="service__title">Fire Alarm<br>Systems</h3>
      <ul class="service__list">
        <li>Experts in fire alarms for safety</li>
        <li>Detects fire and life emergencies</li>
        <li>Certified team</li>
        <li>Fire detection and signaling</li>
      </ul>
    </div>
    <div class="service" style="left:223px; top:375px; width:108px;">
      <h3 class="service__title">Fire Inspections &amp;<br>Confidence<br>Testing</h3>
      <ul class="service__list">
        <li>Nationally Certified Inspection</li>
        <li>Keeps up with local standards</li>
        <li>Provides reports to property</li>
        <li>Lists deficiencies, compliance suggestions</li>
      </ul>
    </div>

    <div class="photo photo--access" role="img" aria-label="Fingerprint access control terminal with a white key card"></div>

    <div class="rail" style="left:23px; top:501px; height:380px;">
      <span class="rail__node" style="top:125px;"></span>
      <span class="rail__node" style="top:371px;"></span>
    </div>
    <h2 class="heading" style="left:32px; top:499px;">ACCESS<br>CON-<br>TROL</h2>

    <div class="service" style="left:36px; top:619px; width:88px;">
      <ul class="service__list">
        <li>Enhances property security</li>
        <li>Controls entry for various premises</li>
        <li>Adds user codes, cameras, auto-locking</li>
        <li>Integrates with automation for remote access</li>
      </ul>
    </div>

    <h2 class="heading" style="left:32px; top:788px;">AUDIO<br>VIDEO</h2>

    <div class="service" style="left:36px; top:870px; width:200px;">
      <ul class="service__list">
        <li>Diverse AV solutions</li>
        <li>Provides projectors, screens, speakers and more</li>
        <li>Tailored solutions for businesses and organizations</li>
        <li>Ensures optimal results with the right system</li>
      </ul>
    </div>

    <footer class="footer">
      <p class="footer__cta">LET US HELP YOU PROTECT YOUR BUSINESS TODAY</p>
      <p class="footer__areas"><span>SERVING</span> AUBURN, KENT,<br>RENTON, SEATTLE, BELLEVUE,<br>LYNNWOOD, MAPLE VALLEY,<br>COVINGTON, PUYALLUP</p>
      <div class="footer__contact">
        <p class="footer__line"><svg width="8" height="8" viewBox="0 0 10 10"><circle cx="5" cy="5" r="5" fill="#fff"/><path d="M3 2.5l1 1-.6.8a4 4 0 0 0 2.3 2.3l.8-.6 1 1-.8.9C4.8 7.6 2.4 5.2 2.1 3.3z" fill="#ec4f4e"/></svg>253-555-0142</p>
        <p class="footer__line"><svg width="8" height="8" viewBox="0 0 10 10"><circle cx="5" cy="5" r="4.3" fill="none" stroke="#fff" stroke-width="1.2"/><rect x="2.8" y="3.4" width="4.4" height="3.2" fill="none" stroke="#fff" stroke-width=".8"/><path d="M2.8 3.4L5 5.2l2.2-1.8" fill="none" stroke="#fff" stroke-width=".8"/></svg>office@bwc-kmo.com</p>
        <p class="footer__line footer__line--addr"><svg width="8" height="9" viewBox="0 0 10 12"><path d="M5 0a4 4 0 0 1 4 4c0 3-4 8-4 8S1 7 1 4a4 4 0 0 1 4-4z" fill="#fff"/><circle cx="5" cy="4" r="1.5" fill="#ec4f4e"/></svg><span>2210 Cedar Ridge Pkwy SE STE 210<br>Harborview, WA 98021</span></p>
      </div>
      <p class="footer__social footer__social--left"><span class="social-mark"></span>bwc_kmo</p>
      <p class="footer__social footer__social--right"><span class="social-mark"></span>BrightwellContractors</p>
    </footer>
  </section>

</div>
</body>
</html>
```